"Drink Champagne and Dance on the Table" sort of business card needed!

We throw events, weddings, engagement parties, baby showers and the sort of end of year corporate events that people remember long after the glitter has settled - the sort of events that make you stand still and say wow when you walk in and then make you want to "Drink Champagne and Dance on the Tables"

We have a great logo with heaps of potential and need a business card that just screams creative professionals!

We are based in Auckland, NZ and are priced at the Premium end of the market were there are around 10 other main competitors. We need to stand out and make a strong statement about who we are!

Our Business Card will be one of the few items that we print out so are fully prepared to invest in a premium print job.

We really love our logo and think it has heaps of potential! Its ok if you would like to manipulate it (maybe put it on an angle, or use the circle element on its own?).

Black and Gold is very striking, but its very done in our market so we would like to avoid a solid black background please

We have done a bit of an inspiration document to give you an idea of the sort of look and feel we are hoping to achieve.

Target Market(s)

Woman aged 30 - 45 with an income bracket of $70k +

Industry/Entity Type

Event Planning

Contact Information for Business Card

Marnie
hello@fennoriwick.co.nz
www.fennoriwick.co.nz
02734419027

Number of Pages Required

5+ page

Requirements
Must have
• Vibrant colours and design (we love the vibrant pink and gold in the inspiration file)
• We would love to see some colour and creativity (although the black and gold is very striking). Because we are doing such minimal print work I am happy for the cards to be a little more expensive so if you want to use cut outs, rounded corners, gold foil, non standard size etc I am happy for that too. I really want the wow factor.
Nice to have
• We would like the design to be double sided.
Should not have
• The logo colour changed
• Use of Purple or Green or solid black background.
• Wedding Photos!

```html
<!DOCTYPE html>
<html lang="en">
<head>
<meta charset="utf-8">
<title>Fenn and Oriwick – Business Card</title>
<link href="https://fonts.googleapis.com/css2?family=Montserrat:wght@400;600&display=swap" rel="stylesheet">
<style>
  :root {
    --backdrop: #ecebe8;
    --card: #ffffff;
    --gold: #c9a232;
    --gold-light: #d8bd7a;
    --foil-a: #9c7a2e;
    --foil-b: #e9d48e;
    --foil-c: #fbf1c4;
    --ink: #555555;
    --icon: #777777;
  }
  * { box-sizing: border-box; margin: 0; padding: 0; }
  html, body { width: 1200px; height: 799px; overflow: hidden; }
  body {
    background: var(--backdrop);
    display: flex;
    align-items: center;
    justify-content: center;
    gap: 40px;
    font-family: "Montserrat", sans-serif;
  }
  .card {
    position: relative;
    width: 540px;
    height: 309px;
    background: var(--card);
    box-shadow: 0 6px 18px rgba(0,0,0,0.15);
    overflow: hidden;
  }
  .foil-band {
    position: absolute;
    top: 0;
    width: 52px;
    height: 100%;
    background: linear-gradient(180deg, var(--foil-a) 0%, var(--foil-b) 45%, var(--foil-c) 75%, var(--foil-b) 100%);
  }
  .card--front .foil-band { right: 0; }
  .card--back .foil-band { left: 0; }

  .brand {
    position: absolute;
    display: flex;
    align-items: center;
    color: var(--gold);
    font-weight: 600;
    white-space: nowrap;
  }
  .brand-dot {
    flex: none;
    border-radius: 50%;
    background: var(--gold);
  }

  .card--front .brand {
    left: 0; right: 52px; top: 0; bottom: 0;
    justify-content: center;
    gap: 14px;
    font-size: 30px;
  }
  .card--front .brand-dot { width: 26px; height: 26px; }

  .card--back .brand {
    right: 30px; top: 62px;
    gap: 10px;
    font-size: 20px;
  }
  .card--back .brand-dot { width: 18px; height: 18px; }

  .holder {
    position: absolute;
    left: 82px; top: 152px;
    font-weight: 600;
    font-size: 24px;
    letter-spacing: 0.04em;
    text-transform: uppercase;
    color: var(--gold-light);
  }
  .contacts {
    position: absolute;
    left: 82px; top: 200px;
    display: grid;
    grid-template-columns: auto auto;
    column-gap: 16px;
    row-gap: 14px;
    font-size: 11.5px;
    color: var(--ink);
  }
  .contact { display: flex; align-items: center; gap: 8px; }
  .contact-icon { width: 15px; height: 15px; flex: none; }
</style>
</head>
<body>

  <section class="card card--front" aria-label="Card front">
    <div class="brand">
      <span class="brand-dot"></span>
      <span class="brand-name">Fenn and Oriwick</span>
    </div>
    <div class="foil-band"></div>
  </section>

  <section class="card card--back" aria-label="Card back">
    <div class="foil-band"></div>
    <div class="brand">
      <span class="brand-dot"></span>
      <span class="brand-name">Fenn and Oriwick</span>
    </div>

    <div class="holder">Marnie</div>

    <div class="contacts">
      <div class="contact">
        <svg class="contact-icon" viewBox="0 0 16 16" aria-hidden="true">
          <circle cx="8" cy="8" r="7.5" fill="var(--icon)"/>
          <path d="M5.4 4.3l1.3-.2.8 1.9-.9.8c.4 1 1.1 1.7 2.1 2.2l.8-.9 1.9.8-.2 1.3c-3.2.2-6-2.6-5.8-5.9z" fill="#fff"/>
        </svg>
        <span>02734419027</span>
      </div>
      <div class="contact">
        <svg class="contact-icon" viewBox="0 0 16 16" aria-hidden="true">
          <circle cx="8" cy="8" r="7.5" fill="var(--icon)"/>
          <circle cx="8" cy="8" r="4" fill="none" stroke="#fff" stroke-width="1"/>
          <ellipse cx="8" cy="8" rx="1.7" ry="4" fill="none" stroke="#fff" stroke-width="0.9"/>
          <line x1="4" y1="8" x2="12" y2="8" stroke="#fff" stroke-width="0.9"/>
        </svg>
        <span>www.fennoriwick.co.nz</span>
      </div>
      <div class="contact">
        <svg class="contact-icon" viewBox="0 0 16 16" aria-hidden="true">
          <circle cx="8" cy="8" r="7.5" fill="var(--icon)"/>
          <rect x="4.2" y="5.3" width="7.6" height="5.4" rx="0.6" fill="#fff"/>
          <path d="M4.4 5.6L8 8.3l3.6-2.7" fill="none" stroke="var(--icon)" stroke-width="0.8"/>
        </svg>
        <span>hello@fennoriwick.co.nz</span>
      </div>
    </div>
  </section>

</body>
</html>
```